We need a modern Google Slides/ PowerPoint presentation for our business brokerage firm in California. Please see attached design colors for colors and fonts- primary colors: white, blue & yellow. On the cover slide we want our logo to be white on blue background (I do not have our logo in white yet, so you can just leave place for logo.) Please limit the amount of stock photos with people. We will insert "Team" photos ourselves, just leave a place for them. Content is attached. Thank you!

```html
<!DOCTYPE html>
<html lang="en">
<head>
<meta charset="utf-8">
<title>Summit Ridge Business Advisors – Presentation</title>
<link rel="stylesheet" href="https://fonts.googleapis.com/css2?family=Poppins:wght@500;600;700&family=Open+Sans:wght@400;600;700&display=swap">
<style>
:root{
  --navy:#13305f;
  --navy-deep:#0f2850;
  --yellow:#ffe900;
  --white:#ffffff;
  --ink:#3a3a3a;
  --board:#e3e3e3;
  --photo-warm:#c9a98a;
  --photo-cool:#9aa8bd;
}
*{margin:0;padding:0;box-sizing:border-box}
html,body{width:1200px;height:3125px;overflow:hidden}
body{background:var(--board);font-family:"Open Sans",sans-serif;color:var(--ink);position:relative}
.hero{position:absolute;left:0;top:0;width:1200px;height:716px;background:linear-gradient(180deg,#c7cad2 0%,#dfe1e6 60%,#e8e8e8 100%)}
.hero-cover{position:absolute;left:220px;top:150px;width:562px;height:316px;transform:scale(1.35);transform-origin:0 0;box-shadow:0 10px 30px rgba(0,0,0,.25)}
.hero-brand{position:absolute;right:78px;top:82px;font:600 24px "Poppins",sans-serif;color:var(--navy);letter-spacing:1px}
.slide{position:absolute;width:562px;height:316px;background:var(--white);overflow:hidden}
.abs{position:absolute}
.photo{position:absolute}
.brand{position:absolute;font:600 9px "Poppins",sans-serif;color:var(--navy);letter-spacing:.5px;white-space:nowrap}
.brand.light{color:var(--white)}
.page-no{position:absolute;right:18px;bottom:12px;font:600 5px "Open Sans",sans-serif;color:var(--navy)}
.page-no.light{color:var(--white)}
.h-title{font:700 22px/1.05 "Poppins",sans-serif;color:var(--navy);letter-spacing:-.3px}
.h-center{text-align:center;width:100%}
.body-text{font:400 8.3px/1.15 "Open Sans",sans-serif;color:var(--ink)}
.body-text p+p{margin-top:6px}
/* cover */
.cover-title{left:29px;top:112px;font:700 23px/1.08 "Poppins",sans-serif;color:var(--white);letter-spacing:-.3px}
.cover-sub{left:29px;top:170px;width:250px;font:400 9px/1.15 "Open Sans",sans-serif;color:var(--white)}
.cover-date{left:29px;top:248px;font:400 6.5px "Open Sans",sans-serif;color:var(--navy)}
.cover-copy{right:30px;top:285px;font:400 4.5px "Open Sans",sans-serif;color:#777}
/* framework */
.fw-sub{top:54px;font:400 7.5px "Open Sans",sans-serif}
.fw-step{position:absolute;top:78px;width:84px}
.fw-pill{position:absolute;left:0;top:0;width:80px;height:22px}
.fw-head{position:absolute;top:33px;right:4px;width:76px;text-align:right;font:700 7.5px/1.05 "Open Sans",sans-serif;color:var(--navy)}
.fw-text{position:absolute;top:58px;left:2px;width:78px;text-align:center;font:400 5px/1.15 "Open Sans",sans-serif;color:#444}
/* services */
.svc{position:absolute;top:94px;width:118px;text-align:center}
.svc-icon{width:58px;height:58px;margin:0 auto}
.svc-head{margin-top:8px;font:700 10px/1.1 "Open Sans",sans-serif;color:var(--navy)}
.svc-text{margin-top:8px;font:400 7.2px/1.15 "Open Sans",sans-serif;color:#444}
.yellow-title{font:700 21px "Poppins",sans-serif;color:var(--yellow);letter-spacing:-.3px}
/* core values */
.cv-label{font:600 10px "Poppins",sans-serif;color:var(--navy)}
.cv-text{font:400 6.3px/1.15 "Open Sans",sans-serif;color:#444}
.cv-left{position:absolute;right:342px;width:150px;text-align:right}
.cv-right{position:absolute;left:340px;width:180px}
/* team */
.member{position:absolute;top:86px;width:150px;text-align:center}
.member-photo{width:76px;height:76px;border-radius:50%;margin:0 auto;background:radial-gradient(circle at 50% 40%,#d9d5d0,#8a8f96);border:3px solid var(--white)}
.member-name{margin-top:12px;font:600 11px "Poppins",sans-serif;color:var(--navy)}
.member-role{font:400 6.5px "Open Sans",sans-serif;color:#444}
.member-bio{margin-top:9px;font:400 6.5px/1.15 "Open Sans",sans-serif;color:#444}
/* contact */
.contact-col{position:absolute;font:400 6.8px/1.2 "Open Sans",sans-serif;color:var(--white)}
.office{font:700 9px "Open Sans",sans-serif;color:var(--yellow);margin-top:12px}
.office:first-child{margin-top:0}
.contact-head{font:600 11.5px "Open Sans",sans-serif;color:var(--white);margin-bottom:14px}
</style>
</head>
<body>

<section class="hero">
  <div class="hero-brand">Summit Ridge</div>
  <div class="slide hero-cover">
    <div class="brand" style="left:29px;top:32px;font-size:15px">Summit Ridge</div>
    <svg class="abs" style="left:0;top:0" width="562" height="316" viewBox="0 0 562 316">
      <polygon points="440,40 562,40 562,100 485,100" fill="var(--yellow)"/>
      <polygon points="0,92 340,92 300,232 0,232" fill="var(--navy)"/>
      <polygon points="0,232 270,232 250,268 0,268" fill="var(--yellow)"/>
      <polygon points="256,232 300,232 275,268" fill="#c8b800"/>
    </svg>
    <div class="photo" role="img" aria-label="Hands signing a business sale agreement with a pen" style="left:300px;top:72px;width:262px;height:158px;clip-path:polygon(45px 0,262px 0,262px 158px,0 158px);background:linear-gradient(135deg,#3b2f2a,#8a7566 50%,#d8d2cc)"></div>
    <div class="abs cover-title">We sell businesses<br>more effectively</div>
    <div class="abs cover-sub">We are a full-service business brokerage &amp; M&amp;A advisory firm in California. With our proven strategic framework, we sell privately held businesses at a greater value and in less time.</div>
    <div class="abs cover-date">Saturday, May 29, 2021</div>
    <div class="abs cover-copy">© 2021 Summit Ridge Business Advisors. All rights reserved.</div>
  </div>
</section>

<!-- 1 cover -->
<div class="slide" style="left:29px;top:733px">
  <div class="brand" style="left:29px;top:32px;font-size:15px">Summit Ridge</div>
  <svg class="abs" style="left:0;top:0" width="562" height="316" viewBox="0 0 562 316">
    <polygon points="440,40 562,40 562,100 485,100" fill="var(--yellow)"/>
    <polygon points="0,92 340,92 300,232 0,232" fill="var(--navy)"/>
    <polygon points="0,232 270,232 250,268 0,268" fill="var(--yellow)"/>
    <polygon points="256,232 300,232 275,268" fill="#c8b800"/>
  </svg>
  <div class="photo" role="img" aria-label="Hands signing a business sale agreement with a pen" style="left:300px;top:72px;width:262px;height:158px;clip-path:polygon(45px 0,262px 0,262px 158px,0 158px);background:linear-gradient(135deg,#3b2f2a,#8a7566 50%,#d8d2cc)"></div>
  <div class="abs cover-title">We sell businesses<br>more effectively</div>
  <div class="abs cover-sub">We are a full-service business brokerage &amp; M&amp;A advisory firm in California. With our proven strategic framework, we sell privately held businesses at a greater value and in less time.</div>
  <div class="abs cover-date">Saturday, May 29, 2021</div>
  <div class="abs cover-copy">© 2021 Summit Ridge Business Advisors. All rights reserved.</div>
</div>

<!-- 2 framework -->
<div class="slide" style="left:609px;top:733px">
  <div class="abs h-title h-center" style="top:24px;font-size:21px">Our Framework</div>
  <div class="abs fw-sub h-center">We’ve helped hundreds of clients to sell their business at higher value by following our strategic framework.</div>
  <div class="fw-step" style="left:18px"><svg class="fw-pill" viewBox="0 0 80 22"><rect x="0" y="3" width="80" height="16" rx="8" fill="var(--yellow)"/><circle cx="22" cy="11" r="11" fill="var(--navy)" stroke="#fff" stroke-width="1.5"/><text x="22" y="15" text-anchor="middle" font-family="Open Sans" font-size="12" fill="#fff">1</text></svg><div class="fw-head">Preparation<br>&amp; Planning</div><div class="fw-text">This phase focuses on preparing your business for sale. Careful preparation makes your business more attractive to buyers and lets you reach the best price for it.</div></div>
  <div class="fw-step" style="left:106px"><svg class="fw-pill" viewBox="0 0 80 22"><rect x="0" y="3" width="80" height="16" rx="8" fill="var(--yellow)"/><circle cx="22" cy="11" r="11" fill="var(--navy)" stroke="#fff" stroke-width="1.5"/><text x="22" y="15" text-anchor="middle" font-family="Open Sans" font-size="12" fill="#fff">2</text></svg><div class="fw-head">Business<br>Valuation</div><div class="fw-text">We advise you on the best methods to determine a price range, gather the key documents and review the factors that drive the value of your business.</div></div>
  <div class="fw-step" style="left:194px"><svg class="fw-pill" viewBox="0 0 80 22"><rect x="0" y="3" width="80" height="16" rx="8" fill="var(--yellow)"/><circle cx="22" cy="11" r="11" fill="var(--navy)" stroke="#fff" stroke-width="1.5"/><text x="22" y="15" text-anchor="middle" font-family="Open Sans" font-size="12" fill="#fff">3</text></svg><div class="fw-head">Marketing<br>the Business</div><div class="fw-text">Once we set the price and sales strategy, we prepare a complete marketing plan and promote your business to qualified buyers while keeping its name confidential.</div></div>
  <div class="fw-step" style="left:282px"><svg class="fw-pill" viewBox="0 0 80 22"><rect x="0" y="3" width="80" height="16" rx="8" fill="var(--yellow)"/><circle cx="22" cy="11" r="11" fill="var(--navy)" stroke="#fff" stroke-width="1.5"/><text x="22" y="15" text-anchor="middle" font-family="Open Sans" font-size="12" fill="#fff">4</text></svg><div class="fw-head">Meet the<br>buyer</div><div class="fw-text">A non-disclosure agreement is signed by all interested buyers. Your business reaches a wide range of buyers, and we only work with those who meet the requirements.</div></div>
  <div class="fw-step" style="left:370px"><svg class="fw-pill" viewBox="0 0 80 22"><rect x="0" y="3" width="80" height="16" rx="8" fill="var(--yellow)"/><circle cx="22" cy="11" r="11" fill="var(--navy)" stroke="#fff" stroke-width="1.5"/><text x="22" y="15" text-anchor="middle" font-family="Open Sans" font-size="12" fill="#fff">5</text></svg><div class="fw-head">Offers &amp;<br>Negotiations</div><div class="fw-text">During this phase we work to produce the best possible offer, evaluating each offer with our knowledge of market trends, financing and negotiation to reach the best terms.</div></div>
  <div class="fw-step" style="left:458px"><svg class="fw-pill" viewBox="0 0 80 22"><rect x="0" y="3" width="80" height="16" rx="8" fill="var(--yellow)"/><circle cx="22" cy="11" r="11" fill="var(--navy)" stroke="#fff" stroke-width="1.5"/><text x="22" y="15" text-anchor="middle" font-family="Open Sans" font-size="12" fill="#fff">6</text></svg><div class="fw-head">Closing</div><div class="fw-text">We work closely with your CPA, landlord, attorney and all relevant third parties to ensure a smooth closing.</div></div>
  <div class="brand" style="left:14px;top:284px">Summit Ridge</div>
  <div class="page-no">2</div>
</div>

<!-- 3 what we do -->
<div class="slide" style="left:29px;top:1068px">
  <div class="abs" style="left:0;top:0;width:562px;height:122px;background:var(--navy)"></div>
  <div class="abs yellow-title h-center" style="top:30px">What we do...</div>
  <div class="svc" style="left:41px"><svg class="svc-icon" viewBox="0 0 58 58"><circle cx="29" cy="29" r="27" fill="var(--navy)" stroke="#fff" stroke-width="2.5"/><rect x="17" y="27" width="5" height="13" fill="#fff"/><path d="M24 27 L30 17 Q33 16 33 20 L32 25 L40 25 Q43 26 42 29 L39 39 Q38 41 36 41 L24 41 Z" fill="#fff"/></svg><div class="svc-head">Exit<br>Planning</div><div class="svc-text">Exit planning strategy will identify the actions that need to be taken so that you can exit your business with confidence.</div></div>
  <div class="svc" style="left:162px"><svg class="svc-icon" viewBox="0 0 58 58"><circle cx="29" cy="29" r="27" fill="var(--navy)" stroke="#fff" stroke-width="2.5"/><circle cx="29" cy="25" r="9" fill="none" stroke="#fff" stroke-width="2"/><rect x="25" y="34" width="8" height="6" fill="#fff"/><line x1="29" y1="21" x2="29" y2="31" stroke="#fff" stroke-width="1.5"/></svg><div class="svc-head">Business<br>Valuations</div><div class="svc-text">By utilizing a variety of valuation methods, we will evaluate your business and determine the most probable selling price.</div></div>
  <div class="svc" style="left:282px"><svg class="svc-icon" viewBox="0 0 58 58"><circle cx="29" cy="29" r="27" fill="var(--navy)" stroke="#fff" stroke-width="2.5"/><rect x="18" y="32" width="5" height="8" fill="#fff"/><rect x="25" y="28" width="5" height="12" fill="#fff"/><rect x="32" y="24" width="5" height="16" fill="#fff"/><path d="M17 27 L27 20 L32 22 L40 16" stroke="#fff" stroke-width="1.8" fill="none"/></svg><div class="svc-head">Seller<br>Representation</div><div class="svc-text">With our proven strategic framework, we’ll help you to sell your business at a greater value and in less time</div></div>
  <div class="svc" style="left:403px"><svg class="svc-icon" viewBox="0 0 58 58"><circle cx="29" cy="29" r="27" fill="var(--navy)" stroke="#fff" stroke-width="2.5"/><path d="M21 17 H37 V25 Q37 32 29 33 Q21 32 21 25 Z" fill="#fff"/><rect x="27" y="33" width="4" height="5" fill="#fff"/><rect x="23" y="38" width="12" height="3" fill="#fff"/></svg><div class="svc-head">Buyer<br>Representation</div><div class="svc-text">From deal sourcing to closing, we guide business buyers through the entire process to set them up for success.</div></div>
  <div class="brand" style="left:14px;top:284px">Summit Ridge</div>
  <div class="page-no">3</div>
</div>

<!-- 4 no upfront costs -->
<div class="slide" style="left:609px;top:1068px;background:var(--navy)">
  <div class="photo" role="img" aria-label="Faint image of a business handshake behind the navy overlay" style="inset:0;background:linear-gradient(120deg,#1a3868,#13305f 60%,#1d3b6a)"></div>
  <div class="brand light h-center" style="top:84px;text-align:center;font-size:12px">Summit Ridge</div>
  <div class="abs yellow-title h-center" style="top:134px;text-align:center;font-size:23px;line-height:1.1">We don’t charge<br>upfront costs.</div>
  <div class="abs" style="left:140px;top:200px;width:282px;text-align:center;font:400 8.4px/1.15 'Open Sans',sans-serif;color:#fff">We are able to deliver world class business brokerage services without upfront costs for our clients. Our fees are success-based. With a success-based pricing model, our commission is earned AFTER the business is sold.</div>
</div>

<!-- 5 preparation -->
<div class="slide" style="left:29px;top:1404px">
  <div class="photo" role="img" aria-label="Hand placing a dart into a dartboard beside a laptop" style="left:39px;top:0;width:245px;height:247px;background:linear-gradient(140deg,#f2f0ee,#cfc8c2 50%,#6d6a66)"></div>
  <div class="abs h-title" style="left:326px;top:62px">Preparation &amp;<br>Planning</div>
  <div class="abs body-text" style="left:326px;top:130px;width:190px">Advanced preparation is the key to success. We help you to prepare your business for sale before it goes on the market. Exit planning strategy will make your business more attractive to the potential buyers and allow you to maximize the value of your business.</div>
  <div class="brand" style="left:14px;top:284px">Summit Ridge</div>
  <div class="page-no">5</div>
</div>

<!-- 6 technology -->
<div class="slide" style="left:609px;top:1404px">
  <div class="photo" role="img" aria-label="Hands holding a tablet showing charts in warm light" style="left:0;top:0;width:282px;height:316px;background:linear-gradient(135deg,#8a5a33,#d79a5c 45%,#f1d3b0)"></div>
  <div class="brand" style="left:282px;width:280px;top:36px;text-align:center">Summit Ridge</div>
  <div class="abs h-title" style="left:282px;width:280px;top:75px;text-align:center">Technology<br>Driven Process</div>
  <div class="abs" style="left:282px;top:158px;width:280px;height:158px;background:var(--navy)"></div>
  <div class="abs" style="left:312px;top:189px;width:220px;text-align:center;font:400 8.4px/1.15 'Open Sans',sans-serif;color:#fff">We have a proven, technology-driven process. It allows us to effectively manage the sales transaction from every angle and move the deal towards closing faster.</div>
  <div class="page-no light">6</div>
</div>

<!-- 7 local market -->
<div class="slide" style="left:29px;top:1739px">
  <div class="abs h-title" style="left:45px;top:44px">Local Market &amp;<br>Industry<br>Knowledge</div>
  <div class="abs body-text" style="left:45px;top:147px;width:195px"><p>We’ve been selling businesses in the Bay Area and Southern California for over 30 years. We know exactly how to effectively market your business in the local market and get it in front of the right buyers faster.</p><p>Our business brokers have a strong grasp of all that goes into the acquisition, operation, and sale of businesses.</p></div>
  <div class="photo" role="img" aria-label="Hand pointing at a tablet with blue charts" style="left:283px;top:0;width:139px;height:316px;background:linear-gradient(160deg,#dde3ee,#a7b3cb 55%,#5a6b93)"></div>
  <div class="abs" style="left:422px;top:0;width:140px;height:316px;background:var(--navy)"></div>
  <div class="brand" style="left:14px;top:284px">Summit Ridge</div>
  <div class="page-no light">7</div>
</div>

<!-- 8 integrity -->
<div class="slide" style="left:609px;top:1739px">
  <div class="abs h-title" style="left:37px;top:35px">Integrity,<br>Commitment &amp;<br>Support</div>
  <div class="abs body-text" style="left:37px;top:120px;width:215px"><p>Our business model is built on transparency, integrity, and commitment. We are committed to the success of each of our clients.</p><p>The process of selling a business is complex and sometimes can be stressful.</p><p>We will be with you every step of the way from preparing business to go on the market to closing. We’ll provide you with the attention and support that you deserve.</p></div>
  <div class="abs" style="left:400px;top:250px;width:162px;height:66px;background:var(--navy)"></div>
  <div class="abs" style="left:524px;top:0;width:38px;height:316px;background:var(--navy)"></div>
  <div class="photo" role="img" aria-label="Two people shaking hands over a desk" style="left:278px;top:0;width:246px;height:250px;background:linear-gradient(135deg,#eef1f6,#bcc6d6 55%,#7d8aa3)"></div>
  <div class="brand" style="left:14px;top:284px">Summit Ridge</div>
  <div class="page-no light">8</div>
</div>

<!-- 9 results -->
<div class="slide" style="left:29px;top:2074px">
  <div class="abs h-title" style="left:45px;top:42px">Results</div>
  <div class="abs body-text" style="left:45px;top:82px;width:145px">At the end of the day, this is about selling your business at the right price to the right buyer and that’s what we do best! We have decades of experience and a proven track record of helping hundreds of business owners.</div>
  <div class="photo" role="img" aria-label="Hands reviewing printed pie and bar charts with a pen" style="left:232px;top:0;width:190px;height:316px;background:linear-gradient(150deg,#2b2623,#9d8e84 40%,#e7e4e2)"></div>
  <div class="abs" style="left:422px;top:0;width:140px;height:316px;background:var(--navy)"></div>
  <div class="brand" style="left:14px;top:284px">Summit Ridge</div>
  <div class="page-no light">9</div>
</div>

<!-- 10 core values -->
<div class="slide" style="left:609px;top:2074px">
  <div class="abs h-title h-center" style="top:22px;font-size:21px">Our Core Values</div>
  <svg class="abs" style="left:232px;top:90px" width="100" height="160" viewBox="0 0 100 160">
    <circle cx="22" cy="20" r="20" fill="var(--navy)"/><circle cx="74" cy="20" r="20" fill="var(--navy)"/>
    <circle cx="22" cy="78" r="20" fill="var(--navy)"/><circle cx="74" cy="78" r="20" fill="var(--navy)"/>
    <circle cx="22" cy="136" r="20" fill="var(--navy)"/><circle cx="74" cy="136" r="20" fill="var(--navy)"/>
    <rect x="12" y="19" width="4" height="10" fill="#fff"/><path d="M18 19 L23 11 Q26 10 26 13 L25 17 L31 17 Q33 18 32 20 L30 28 L18 28 Z" fill="#fff"/>
    <path d="M67 11 H81 V17 Q81 23 74 24 Q67 23 67 17 Z" fill="#fff"/><rect x="72" y="24" width="4" height="4" fill="#fff"/><rect x="69" y="28" width="10" height="2.5" fill="#fff"/>
    <circle cx="22" cy="75" r="7" fill="none" stroke="#fff" stroke-width="1.8"/><rect x="19" y="82" width="6" height="5" fill="#fff"/>
    <circle cx="69" cy="74" r="4" fill="#fff"/><rect x="64" y="79" width="10" height="8" rx="3" fill="#fff"/><rect x="76" y="69" width="8" height="6" rx="1" fill="#fff"/>
    <rect x="13" y="139" width="4" height="6" fill="#fff"/><rect x="19" y="135" width="4" height="10" fill="#fff"/><rect x="25" y="131" width="4" height="14" fill="#fff"/><path d="M12 134 L20 128 L24 130 L31 125" stroke="#fff" stroke-width="1.5" fill="none"/>
    <circle cx="74" cy="136" r="8" fill="none" stroke="#fff" stroke-width="3" stroke-dasharray="3 2"/><circle cx="74" cy="136" r="3.5" fill="#fff"/>
  </svg>
  <div class="cv-left" style="top:96px"><div class="cv-label">Commitment</div><div class="cv-text">We are dedicated to<br>our client’s success</div></div>
  <div class="cv-left" style="top:154px"><div class="cv-label">Innovation</div><div class="cv-text">We are constantly looking for ways<br>to improve efficiency and effectiveness.</div></div>
  <div class="cv-left" style="top:212px"><div class="cv-label">Results</div><div class="cv-text">We motivated, passionate committed<br>to produce the best results for our clients</div></div>
  <div class="cv-right" style="top:94px"><div class="cv-label">Integrity</div><div class="cv-text">We are committed to perform with integrity and professionalism.</div></div>
  <div class="cv-right" style="top:152px"><div class="cv-label">Compassion</div><div class="cv-text">Our team recognizes that selling a business is more than just a financial transaction. We guide and support our clients every step of the way.</div></div>
  <div class="cv-right" style="top:210px"><div class="cv-label">Passion</div><div class="cv-text">We are passionate about small businesses and entrepreneurship.</div></div>
  <div class="brand" style="left:14px;top:284px">Summit Ridge</div>
  <div class="page-no">10</div>
</div>

<!-- 11 team -->
<div class="slide" style="left:29px;top:2408px">
  <div class="abs" style="left:0;top:0;width:562px;height:124px;background:var(--navy)"></div>
  <div class="abs yellow-title h-center" style="top:26px;text-align:center">Our Team</div>
  <div class="member" style="left:38px"><div class="member-photo" role="img" aria-label="Space for team member photo"></div><div class="member-name">Person Name</div><div class="member-role">Job Title Goes Here!</div><div class="member-bio">Short biography of this team member, their background in business sales and the clients they help across the region.</div></div>
  <div class="member" style="left:206px"><div class="member-photo" role="img" aria-label="Space for team member photo"></div><div class="member-name">Person Name</div><div class="member-role">Job Title Goes Here!</div><div class="member-bio">Short biography of this team member, their background in business sales and the clients they help across the region.</div></div>
  <div class="member" style="left:375px"><div class="member-photo" role="img" aria-label="Space for team member photo"></div><div class="member-name">Person Name</div><div class="member-role">Job Title Goes Here!</div><div class="member-bio">Short biography of this team member, their background in business sales and the clients they help across the region.</div></div>
  <div class="brand" style="left:14px;top:284px">Summit Ridge</div>
  <div class="page-no">11</div>
</div>

<!-- 12 partner -->
<div class="slide" style="left:609px;top:2408px">
  <div class="photo" role="img" aria-label="Business handshake over a soft network graphic" style="left:39px;top:0;width:246px;height:248px;background:linear-gradient(145deg,#f3f5f8,#c8d0dc 55%,#8a97ab)"></div>
  <div class="abs h-title" style="left:326px;top:62px">Ready to partner<br>with us?</div>
  <div class="abs body-text" style="left:326px;top:112px;width:195px">Book a time that works for you for a confidential consultation with one of our business brokers. We are looking forward to talking with you about how we can help you to achieve your goals and successfully exit your business.</div>
  <div class="brand" style="left:14px;top:284px">Summit Ridge</div>
  <div class="page-no">12</div>
</div>

<!-- 13 contact -->
<div class="slide" style="left:319px;top:2743px;background:var(--navy)">
  <div class="brand light" style="left:64px;top:156px;font-size:13px">Summit Ridge</div>
  <div class="contact-col" style="left:225px;top:30px;width:140px">
    <div class="contact-head">Contact Us</div>
    <div class="office">Oakland Office</div><div>4120 Harborview Dr.<br>Ste# 110<br>Oakland,CA 94621</div>
    <div class="office">Dublin Office</div><div>7850 Amador Ave.<br>#140<br>Dublin,CA 94568</div>
    <div class="office">Walnut Creek</div><div>390 Oak Grove Rd. Suite A12<br>Walnut Creek, CA 94596</div>
    <div style="margin-top:8px">925-555-0142<br>Fax: 925-555-0143</div>
  </div>
  <div class="contact-col" style="left:374px;top:30px;width:160px">
    <div class="office">Sacramento Office</div><div>2215 Riverside Way<br>Ste#310<br>Sacramento,CA 95825</div>
    <div class="office">San Francisco Office</div><div>880 Presidio St.<br>Ste# 402<br>San Francisco,CA 94115</div>
    <div class="office">Southern California</div><div>15400 Valley Crest Blvd, Ste# 220<br>Encino,CA 91436<br>661-555-0178</div>
    <div style="margin-top:8px">415 W. Sierra Blvd.<br>#6 Lancaster,CA 93534<br>818-555-0126<br>Fax: 661-555-0190</div>
  </div>
</div>

</body>
</html>
```